Experienced Home remodel service

I'm a home remodeler. I want a catch phrase that clearly describes viewers what kind of work I'm in like the purple phrase on my rough draft idea. I need my website, phone, logo, slogan included. The picture is of my daughter. I want her on it. Be cool if something could be added to her picture like a hard hat or tool belt ect and her picture cut out/background removed. Some kind of background other than plain white for whole picture. I added extra pics of her so pick one

Target Market(s)

Home owners between 30-60

Industry/Entity Type

Home renovation/remodel

Colors

Designer to choose colors to be used in the design.

Requirements
Must have
• Daughters picture incorporated. Logo, phone, website address, slogan,
Nice to have
• See a hardhat or tool belt added to one of my daughters pictures that is chosen to use by designer

```html
<!DOCTYPE html>
<html lang="en">
<head>
<meta charset="utf-8">
<title>Harlow Home Solutions – Banner</title>
<link rel="stylesheet" href="https://fonts.googleapis.com/css2?family=Oswald:wght@500&family=Montserrat:wght@500;600&display=swap">
<style>
  :root{
    --page:#ececec;
    --ink:#0a0a0a;
    --paper:#ffffff;
    --band:#bdbdbd;
    --soft-light:#f4f4f4;
    --soft-mid:#e4e4e4;
    --portrait-a:#d9c6ea;
    --portrait-b:#b9a3d3;
  }
  *{margin:0;padding:0;box-sizing:border-box}
  html,body{width:1200px;height:900px;overflow:hidden;background:var(--page)}
  .banner{position:absolute;left:92px;top:176px;width:1016px;height:506px;background:var(--paper);overflow:hidden}
  .room-backdrop{position:absolute;left:0;top:0;width:500px;height:506px;
    background:linear-gradient(160deg,var(--soft-light) 0%,var(--soft-mid) 60%,var(--soft-light) 100%)}
  .dark-panel{position:absolute;inset:0;background:var(--ink);
    clip-path:polygon(371px 0,1016px 0,1016px 506px,488px 506px)}
  .brand-mark{position:absolute;left:128px;top:70px;display:flex;align-items:center;gap:14px;
    font-family:"Oswald",sans-serif;font-weight:500;font-size:64px;color:var(--ink);line-height:1}
  .brand-mark .dot{width:22px;height:22px;background:var(--ink)}
  .slogan{position:absolute;left:60px;top:232px;width:300px;text-align:center;
    font-family:"Oswald",sans-serif;font-weight:500;color:var(--ink);line-height:1}
  .slogan .lead{display:block;font-size:46px}
  .slogan .home{display:block;font-size:78px;margin-top:8px}
  .phone-bar{position:absolute;left:0;top:402px;width:463px;height:58px;background:var(--ink);
    display:flex;align-items:center;gap:14px;padding-left:48px;
    font-family:"Montserrat",sans-serif;font-weight:500;font-size:38px;color:var(--paper)}
  .phone-bar svg{width:44px;height:44px;flex:none}
  .website{position:absolute;left:80px;top:474px;font-family:"Montserrat",sans-serif;font-weight:500;
    font-size:14px;letter-spacing:1.5px;color:var(--ink)}
  .company-name{position:absolute;left:448px;top:12px;font-family:"Oswald",sans-serif;font-weight:500;
    font-size:112px;line-height:1;color:var(--paper);letter-spacing:1px}
  .name-band{position:absolute;z-index:2;left:391px;top:142px;width:420px;height:67px;background:var(--band);
    font-family:"Oswald",sans-serif;font-weight:500;font-size:48px;line-height:67px;color:var(--ink);
    padding-left:56px;white-space:nowrap}
  .services{list-style:none}
  .service{position:absolute;display:flex;align-items:center;gap:26px;
    font-family:"Montserrat",sans-serif;font-weight:500;font-size:44px;color:var(--paper)}
  .service .badge{width:66px;height:66px;border-radius:50%;background:var(--paper);border:3px solid var(--ink);
    box-shadow:0 0 0 3px var(--paper);display:flex;align-items:center;justify-content:center}
  .service .badge svg{width:40px;height:40px}
  .service.build{left:406px;top:236px}
  .service.repair{left:423px;top:317px}
  .service.replace{left:448px;top:398px}
  .portrait{position:absolute;z-index:1;left:733px;top:124px;width:244px;height:382px;border-radius:110px 110px 0 0;
    background:linear-gradient(180deg,var(--portrait-a),var(--portrait-b))}
</style>
</head>
<body>
  <section class="banner">
    <div class="room-backdrop" role="img" aria-label="Faded photo of a bright modern living room"></div>
    <div class="dark-panel"></div>

    <div class="brand-mark"><span class="dot"></span>HARLOW</div>

    <p class="slogan"><span class="lead">FOR ALL YOUR</span><span class="home">HOME</span></p>

    <div class="phone-bar">
      <svg viewBox="0 0 44 44" aria-hidden="true">
        <circle cx="22" cy="22" r="19" fill="none" stroke="#fff" stroke-width="3"/>
        <path d="M15 12c2-1 3 0 4 3l1 3c0 1-1 2-2 3 1 3 3 5 6 6 1-1 2-2 3-2l3 1c3 1 4 2 3 4-1 3-4 4-7 3-6-2-11-7-13-13-1-3 0-6 2-8z" fill="#fff"/>
      </svg>
      <span>555-014-2270</span>
    </div>
    <p class="website">www.harlowhomesolutions.com</p>

    <h1 class="company-name">HARLOW</h1>

    <div class="portrait" role="img" aria-label="Cut-out photo of the owner's young daughter in a yellow hard hat and lilac puffer jacket holding a hammer"></div>

    <div class="name-band">HOME SOLUTIONS</div>

    <ul class="services">
      <li class="service build">
        <span class="badge"><svg viewBox="0 0 40 40" aria-hidden="true">
          <circle cx="11" cy="7" r="4" fill="#000"/>
          <path d="M7 13h8l3 8-3 1v14h-3v-9h-2v9H7z" fill="#000"/>
          <path d="M21 24h8v4h-8zM30 24h8v4h-8zM21 29h4v4h-4zM26 29h8v4h-8zM35 29h3v4h-3zM21 34h8v4h-8zM30 34h8v4h-8z" fill="#000"/>
        </svg></span>Build
      </li>
      <li class="service repair">
        <span class="badge"><svg viewBox="0 0 40 40" aria-hidden="true">
          <circle cx="24" cy="18" r="9" fill="none" stroke="#000" stroke-width="4" stroke-dasharray="4 3"/>
          <circle cx="24" cy="18" r="3" fill="#000"/>
          <path d="M4 36l12-12" stroke="#000" stroke-width="5" stroke-linecap="round"/>
          <path d="M8 4a6 6 0 0 0 7 8" fill="none" stroke="#000" stroke-width="3"/>
        </svg></span>Repair
      </li>
      <li class="service replace">
        <span class="badge"><svg viewBox="0 0 40 40" aria-hidden="true">
          <path d="M6 14h24M24 8l7 6-7 6M34 26H10M16 20l-7 6 7 6" fill="none" stroke="#000" stroke-width="4" stroke-linejoin="round"/>
        </svg></span>Replace
      </li>
    </ul>
  </section>
</body>
</html>
```